Tevrix BIM business website

I have a logo design and business card concept is ongoing at this point, but i need a website design based on VDC or BIM ("Virtual Building and Construction" or "Building Information Modeling") that will stand out for the quality and concept that we provide. I am a consultant providing training and production work for Quorvel (Zembrick application <where most of the overview can be obtained>). We are providing BIM production and coordination services as well. I can fill in the meat but I need an open development website. Currently, just obtaining a domain so it can be included on a business card is the quickest objective, then developing the content and launching it.

Business

```html
<!DOCTYPE html>
<html lang="en">
<head>
<meta charset="utf-8">
<title>Tevrix BIM Business</title>
<link href="https://fonts.googleapis.com/css2?family=Roboto:wght@300;400;500;700&family=Roboto+Condensed:wght@700&display=swap" rel="stylesheet">
<style>
:root{
  --orange:#f2a21d;
  --navy:#26326a;
  --navy-deep:#1d2656;
  --ink:#333;
  --muted:#666;
  --light:#f3f3f3;
  --line:#e3e3e3;
  --footer:#3e3e3e;
  --footer-base:#2b2b2b;
  --white:#fff;
}
*{margin:0;padding:0;box-sizing:border-box}
html,body{width:1200px;height:3435px;overflow:hidden;background:var(--white)}
body{font-family:'Roboto',Arial,sans-serif;color:var(--ink);position:relative}
.abs{position:absolute}
p{line-height:1.55}

/* hero */
.hero{position:absolute;left:0;top:0;width:1200px;height:527px;overflow:hidden;
  background:linear-gradient(180deg,#3a4a6a 0%,#27324b 45%,#1d1f26 80%,#3a2a20 100%)}
.hero-photo{position:absolute;inset:0;background:
  linear-gradient(90deg,rgba(20,30,60,.55),rgba(20,30,60,.1) 50%,rgba(20,30,60,.5)),
  linear-gradient(180deg,rgba(120,140,170,.25),rgba(0,0,0,.2))}
.hero-corner{position:absolute;left:0;top:0}
.topbar{position:absolute;left:0;top:0;width:1200px;height:60px;background:linear-gradient(180deg,#fff,#e6e6e6)}
.nav{position:absolute;right:150px;top:22px;display:flex;gap:38px;font-size:12px;color:#444;letter-spacing:.3px}
.brand{position:absolute;left:30px;top:22px;display:flex;align-items:center;gap:10px;color:var(--white)}
.brand-mark{width:22px;height:22px;border-radius:50%;background:var(--orange)}
.brand-name{font-size:30px;font-weight:700;line-height:1}
.brand-sub{position:absolute;left:30px;top:98px;font-size:11px;font-weight:700;letter-spacing:2px;color:var(--white)}
.hero-title{position:absolute;top:200px;width:1200px;text-align:center;color:var(--white);font-size:34px;font-weight:700;letter-spacing:.5px}
.hero-sub{position:absolute;top:258px;width:1200px;text-align:center;color:var(--orange);font-size:22px;letter-spacing:.4px}
.btn{position:absolute;left:529px;top:311px;width:142px;height:42px;background:var(--navy);color:var(--white);
  font-size:13px;font-weight:500;display:flex;align-items:center;justify-content:center;border-radius:2px}

/* experience */
.exp-head{left:160px;top:596px;font-size:30px;font-weight:700;color:var(--orange)}
.exp-head b{font-family:'Roboto Condensed',sans-serif;color:var(--navy);font-size:54px;vertical-align:-6px;margin:0 2px}
.exp-brief{left:160px;top:682px;font-size:22px;color:var(--navy)}
.exp-brief span{color:var(--orange)}
.exp-text{left:160px;top:716px;width:440px;font-size:12.5px;color:var(--muted)}
.exp-text p+p{margin-top:12px}
.learn{left:160px;top:844px;font-size:11.5px;color:#555;display:flex;align-items:center;gap:8px;border-bottom:1px solid #999}
.exp-frame{left:650px;top:592px;width:367px;height:286px;border:1px solid var(--line)}
.exp-photo{left:673px;top:568px;width:367px;height:286px;background:linear-gradient(160deg,#9fc7e8 0%,#c8dcec 40%,#6a5848 70%,#4c6a3a 100%)}
.slider-arrow{width:28px;height:28px;border-radius:50%;background:rgba(0,0,0,.35);display:flex;align-items:center;justify-content:center}

/* section title */
.sec-title{position:absolute;width:1200px;text-align:center;font-size:30px;font-weight:700;color:var(--orange)}
.sec-rule{position:absolute;left:540px;width:120px;height:2px;background:#d6d6d6}
.sec-intro{position:absolute;width:1200px;text-align:center;font-size:12.5px;color:var(--muted);line-height:1.5}

/* specialization */
.spec{position:absolute;left:0;top:905px;width:1200px;height:332px;background:linear-gradient(180deg,#f8f8f8,#efefef)}
.spec-item{position:absolute;top:1037px;width:119px;text-align:center}
.spec-box{width:119px;height:119px;background:var(--white);border:1px solid var(--line);display:flex;align-items:center;justify-content:center}
.spec-label{margin-top:14px;font-size:11.5px;font-weight:500;color:#444}

/* projects strip */
.projects{position:absolute;left:0;top:1241px;width:1200px;height:316px;display:flex}
.project{flex:1;position:relative;display:flex;flex-direction:column;align-items:center;justify-content:center;color:var(--white)}
.project h3{font-size:30px;font-weight:700}
.project span{font-size:30px;font-weight:300}
.project.plain h3,.project.plain span{visibility:hidden}

/* about */
.about-photo{left:137px;top:1740px;width:413px;height:344px;background:radial-gradient(ellipse at 60% 50%,#d9c7a6 0%,#e9e6e0 40%,#fff 75%)}
.feat{position:absolute;left:595px;display:flex;gap:30px}
.feat-icon{width:62px;height:62px;border-radius:50%;background:var(--white);border:1px solid var(--line);display:flex;align-items:center;justify-content:center;box-shadow:0 2px 6px rgba(0,0,0,.06)}
.feat h4{font-size:13.5px;font-weight:500;color:var(--navy);margin-top:4px}
.feat p{font-size:12px;color:var(--muted);margin-top:8px;width:330px}

/* blog */
.blog{position:absolute;left:0;top:2146px;width:1200px;height:373px;background:linear-gradient(180deg,#f6f6f6,#eeeeee)}
.blog-intro{left:160px;top:2173px;width:257px;height:296px;background:var(--navy);color:var(--white);text-align:center;padding-top:60px}
.blog-intro h3{font-size:30px;font-weight:700;margin-top:18px}
.blog-intro p{font-size:12px;margin:18px 24px 0;opacity:.9;line-height:1.45}
.post{position:absolute;top:2187px;width:266px;height:282px;background:var(--white)}
.post-photo{width:266px;height:176px;background:linear-gradient(180deg,#5f8fc5 0%,#9bbde0 45%,#e8e2d8 65%,#7e8a76 100%)}
.post-date{position:absolute;left:24px;top:-15px;width:56px;height:58px;background:var(--orange);color:#222;text-align:center;font-weight:700;line-height:1}
.post-date b{display:block;font-size:24px;padding-top:8px}
.post-date small{font-size:10px}
.post h4{font-size:13.5px;font-weight:500;margin:26px 14px 0;color:#222}
.post p{font-size:12px;color:var(--muted);margin:6px 14px 0;line-height:1.45}

/* testimonials */
.testi{position:absolute;top:2663px;width:284px;height:245px;background:var(--light);text-align:center}
.avatar{position:absolute;left:106px;top:-36px;width:72px;height:72px;border-radius:50%;background:linear-gradient(180deg,#dfe6ef,#b9c6d6);border:3px solid var(--white)}
.testi h4{margin-top:58px;font-size:15px;font-weight:700;color:var(--navy)}
.testi small{display:block;font-size:9.5px;color:#777;margin-top:4px}
.testi p{font-size:12px;color:#555;margin:24px 18px 0;text-align:justify;line-height:1.5}
.dots{position:absolute;left:565px;top:2919px;display:flex;gap:9px}
.dots i{width:13px;height:13px;border-radius:50%;border:1px solid #ccc;display:block}

/* contact band */
.contact-band{position:absolute;left:0;top:2989px;width:1200px;height:119px;background:var(--orange)}
.contact{position:absolute;top:3018px;display:flex;align-items:center;gap:18px;color:var(--white)}
.contact-icon{width:64px;height:64px;border-radius:50%;background:var(--white);display:flex;align-items:center;justify-content:center}
.contact-text{font-size:11.5px;line-height:1.45}

/* footer */
.footer{position:absolute;left:0;top:3108px;width:1200px;height:263px;background:var(--footer);color:#ddd}
.foot-brand{left:160px;top:3150px;width:240px;height:120px;background:radial-gradient(ellipse at 50% 50%,#6a6a6a,#3e3e3e 70%);display:flex;flex-direction:column;align-items:center;justify-content:center}
.foot-brand .name{font-size:30px;font-weight:700;color:#ddd;display:flex;align-items:center;gap:10px}
.foot-brand .name i{width:20px;height:20px;border-radius:50%;background:#bbb;display:block}
.foot-brand .tag{font-size:11px;letter-spacing:2px;margin-top:6px;color:#ddd;font-weight:700}
.foot-about{left:160px;top:3283px;width:210px;font-size:12px;color:#ddd;line-height:1.45}
.foot-h{position:absolute;top:3144px;font-size:15px;font-weight:700;color:var(--white)}
.foot-list{position:absolute;top:3188px;list-style:none;font-size:12px;color:#ddd}
.foot-list li{margin-bottom:13px}
.recent{position:absolute;left:770px;width:260px}
.recent h5{font-size:12px;font-weight:500;color:var(--orange)}
.recent p{font-size:10.5px;color:#ccc;line-height:1.45;margin-top:4px}
.copyright{position:absolute;left:0;top:3371px;width:1200px;height:64px;background:var(--footer-base);color:#999;font-size:10.5px;text-align:center;line-height:64px}
</style>
</head>
<body>

<!-- hero -->
<section class="hero" role="img" aria-label="City skyline of glass office towers at dusk">
  <div class="hero-photo"></div>
  <div class="topbar"></div>
  <svg class="hero-corner" width="345" height="150" viewBox="0 0 345 150">
    <polygon points="0,0 345,0 185,150 0,150" fill="#26326a"/>
    <polygon points="0,0 220,0 75,150 0,150" fill="#1d2656" opacity=".6"/>
  </svg>
</section>
<div class="brand"><span class="brand-mark"></span><span class="brand-name">Tevrix</span></div>
<div class="brand-sub">BIM CONSULTING</div>
<nav class="nav"><span>ABOUT US</span><span>SERVICES</span><span>PROJECTS</span><span>CONSTRUCTION WORK</span><span>CONTACT US</span></nav>
<h1 class="hero-title">TEVRIX BIM BUSINESS</h1>
<div class="hero-sub">VIRTUAL BUILDING AND CONSTRUCTION</div>
<a class="btn">CONTACT US</a>

<!-- experience -->
<h2 class="abs exp-head">Over<b>25</b>years of Experience</h2>
<h3 class="abs exp-brief" style="font-weight:400">A brief about <span>Tevrix</span></h3>
<div class="abs exp-text">
  <p>Lorem Ipsum is simply dummy text of the printing and typesetting industry. Lorem Ipsum has been the industry's standard dummy text ever since the 1500s, when an unknown printer.</p>
  <p>It has survived not only five centuries, but also the leap into electronic typesetting, remaining essentially unchanged.</p>
</div>
<a class="abs learn">Learn more
  <svg width="14" height="8" viewBox="0 0 14 8"><path d="M0 4h12M9 1l3 3-3 3" stroke="#555" fill="none" stroke-width="1.3"/></svg></a>
<div class="abs exp-frame"></div>
<div class="abs exp-photo" role="img" aria-label="Modern two-storey glass house with lawn">
  <div class="abs slider-arrow" style="left:12px;top:129px"><svg width="10" height="10"><path d="M7 1L3 5l4 4" stroke="#fff" fill="none" stroke-width="1.5"/></svg></div>
  <div class="abs slider-arrow" style="right:12px;top:129px"><svg width="10" height="10"><path d="M3 1l4 4-4 4" stroke="#fff" fill="none" stroke-width="1.5"/></svg></div>
</div>

<!-- specialization -->
<section class="spec" role="img" aria-label="Faint line sketch of city buildings in the background"></section>
<h2 class="sec-title" style="top:926px">Our Specialization</h2>
<div class="sec-rule" style="top:972px"></div>
<p class="sec-intro" style="top:982px">Lorem Ipsum is simply dummy text of the printing and typesetting industry.<br>Lorem Ipsum has been the industry's standard dummy text ever since the 1500s.</p>

<div class="spec-item" style="left:160px"><div class="spec-box">
  <svg width="54" height="54" viewBox="0 0 54 54" fill="none" stroke="#f2a21d" stroke-width="2"><rect x="8" y="14" width="28" height="16" rx="2"/><path d="M36 20h12M14 30v16h10V30"/></svg></div><div class="spec-label">CONSTRUCTION</div></div>
<div class="spec-item" style="left:311px"><div class="spec-box">
  <svg width="54" height="54" viewBox="0 0 54 54" fill="none" stroke="#aaa" stroke-width="2"><rect x="14" y="6" width="26" height="12" rx="2"/><path d="M27 18v30"/></svg></div><div class="spec-label">RENOVATION</div></div>
<div class="spec-item" style="left:463px"><div class="spec-box">
  <svg width="54" height="54" viewBox="0 0 54 54" fill="none" stroke="#aaa" stroke-width="2"><path d="M14 6v42h28v-8H22V6z"/></svg></div><div class="spec-label">CONSULTING</div></div>
<div class="spec-item" style="left:614px"><div class="spec-box">
  <svg width="54" height="54" viewBox="0 0 54 54" fill="none" stroke="#aaa" stroke-width="2"><path d="M10 44L34 20M20 44l24-24M30 10l14 14M12 10l8 8"/></svg></div><div class="spec-label">CONSTRUCTOR</div></div>
<div class="spec-item" style="left:765px"><div class="spec-box">
  <svg width="54" height="54" viewBox="0 0 54 54" fill="none" stroke="#aaa" stroke-width="2"><rect x="10" y="16" width="14" height="32"/><rect x="26" y="6" width="18" height="42"/><path d="M30 14h10M30 22h10M30 30h10"/></svg></div><div class="spec-label">ARCHITECTURE</div></div>
<div class="spec-item" style="left:916px"><div class="spec-box">
  <svg width="54" height="54" viewBox="0 0 54 54" fill="none" stroke="#aaa" stroke-width="2"><path d="M10 44L44 10M10 10l34 34M38 6l10 10"/></svg></div><div class="spec-label">PLANNING</div></div>

<!-- projects -->
<section class="projects">
  <div class="project" style="background:linear-gradient(160deg,#5a4a3e,#2f2a28)" role="img" aria-label="Dark modern building exterior"><h3>Project</h3><span>Goes here</span></div>
  <div class="project plain" style="background:linear-gradient(180deg,#8fb2d8,#c9b59a 60%,#6b6152)" role="img" aria-label="Tall residential tower with balconies"><h3>Project</h3><span>Goes here</span></div>
  <div class="project" style="background:linear-gradient(160deg,#7a6550,#3e342c)" role="img" aria-label="Angular contemporary building"><h3>Featured</h3><span>Work</span></div>
  <div class="project" style="background:linear-gradient(160deg,#5e6b78,#34383e)" role="img" aria-label="Glass office tower from below"><h3>Tevrix</h3><span>Project</span></div>
  <div class="project" style="background:linear-gradient(160deg,#4a5a72,#2a3340 70%,#3c4a2e)" role="img" aria-label="Office buildings with lawn"><h3>Project</h3><span>Goes here</span></div>
</section>

<!-- about -->
<h2 class="sec-title" style="top:1626px">About us</h2>
<div class="sec-rule" style="top:1672px"></div>
<p class="sec-intro" style="top:1690px">Lorem Ipsum is simply dummy text of the printing and typesetting industry.<br>Lorem Ipsum has been the industry's standard dummy text ever since the 1500s.</p>
<div class="abs about-photo" role="img" aria-label="Construction worker in hard hat kneeling beside a house frame model"></div>

<div class="feat" style="top:1766px"><div class="feat-icon">
  <svg width="30" height="30" viewBox="0 0 30 30" fill="none" stroke="#f2a21d" stroke-width="2"><path d="M4 20a11 11 0 0 1 22 0M2 20h26v4H2z"/></svg></div>
  <div><h4>Virtual Building and Construction</h4><p>Lorem Ipsum is simply dummy text of the printing and typesetting industry.</p></div></div>
<div class="feat" style="top:1886px"><div class="feat-icon">
  <svg width="30" height="30" viewBox="0 0 30 30" fill="none" stroke="#f2a21d" stroke-width="2"><rect x="8" y="3" width="14" height="8" rx="1"/><path d="M15 11v16"/></svg></div>
  <div><h4>Building Information Modeling</h4><p>Lorem Ipsum is simply dummy text of the printing and typesetting industry.</p></div></div>
<div class="feat" style="top:2006px"><div class="feat-icon">
  <svg width="30" height="30" viewBox="0 0 30 30" fill="none" stroke="#f2a21d" stroke-width="2"><rect x="4" y="7" width="17" height="9" rx="1"/><path d="M21 10h6M8 16v10h6V16"/></svg></div>
  <div><h4>BIM production and Coordination</h4><p>Lorem Ipsum is simply dummy text of the printing and typesetting industry.</p></div></div>

<!-- blog -->
<section class="blog"></section>
<div class="abs blog-intro">
  <svg width="70" height="60" viewBox="0 0 70 60"><path d="M8 6h46a6 6 0 0 1 6 6v24a6 6 0 0 1-6 6H26l-14 12v-12H8a6 6 0 0 1-6-6V12a6 6 0 0 1 6-6z" fill="#fff"/><circle cx="20" cy="24" r="3.5" fill="#26326a"/><circle cx="31" cy="24" r="3.5" fill="#26326a"/><circle cx="42" cy="24" r="3.5" fill="#26326a"/></svg>
  <h3>From Blog</h3>
  <p>Lorem Ipsum is simply dummy text of the printing and typesetting industry.</p>
</div>
<article class="post" style="left:488px">
  <div class="post-photo" role="img" aria-label="Curved modern hotel building under blue sky"></div>
  <div class="post-date"><b>14</b><small>MAR</small></div>
  <h4>Modern Architecture Design</h4>
  <p>Lorem Ipsum is simply dummy text of the printing and typesetting industry.</p>
</article>
<article class="post" style="left:774px">
  <div class="post-photo" role="img" aria-label="Curved modern hotel building under blue sky"></div>
  <div class="post-date"><b>14</b><small>MAR</small></div>
  <h4>Modern Architecture Design</h4>
  <p>Lorem Ipsum is simply dummy text of the printing and typesetting industry.</p>
</article>

<!-- testimonials -->
<h2 class="sec-title" style="top:2552px">Testimonials</h2>
<div class="sec-rule" style="top:2598px"></div>
<div class="testi" style="left:158px"><div class="avatar" role="img" aria-label="Client portrait"></div>
  <h4>Daniel Reyes</h4><small>Halden Works Inc.</small>
  <p>Lorem Ipsum is simply dummy text of the printing and typesetting industry. Lorem Ipsum is simply dummy text of the printing and typesetting industry. Lorem Ipsum is simply dummy text.</p></div>
<div class="testi" style="left:456px"><div class="avatar" role="img" aria-label="Client portrait"></div>
  <h4>Daniel Reyes</h4><small>Halden Works Inc.</small>
  <p>Lorem Ipsum is simply dummy text of the printing and typesetting industry. Lorem Ipsum is simply dummy text of the printing and typesetting industry. Lorem Ipsum is simply dummy text.</p></div>
<div class="testi" style="left:756px"><div class="avatar" role="img" aria-label="Client portrait"></div>
  <h4>Daniel Reyes</h4><small>Halden Works Inc.</small>
  <p>Lorem Ipsum is simply dummy text of the printing and typesetting industry. Lorem Ipsum is simply dummy text of the printing and typesetting industry. Lorem Ipsum is simply dummy text.</p></div>
<div class="dots"><i></i><i></i><i></i><i></i></div>

<!-- contact band -->
<section class="contact-band"></section>
<div class="contact" style="left:158px"><div class="contact-icon">
  <svg width="28" height="28" viewBox="0 0 28 28" fill="none" stroke="#f2a21d" stroke-width="2"><path d="M7 3l4 6-3 3a15 15 0 0 0 8 8l3-3 6 4-3 5C12 25 3 16 2 6z"/></svg></div>
  <div class="contact-text">Phone<br>+1 555 014 2290</div></div>
<div class="contact" style="left:480px"><div class="contact-icon">
  <svg width="28" height="28" viewBox="0 0 28 28" fill="none" stroke="#f2a21d" stroke-width="2"><path d="M14 26s-8-9-8-15a8 8 0 0 1 16 0c0 6-8 15-8 15z"/><circle cx="14" cy="11" r="3"/></svg></div>
  <div class="contact-text">Tevrix bim business<br>Dummy address</div></div>
<div class="contact" style="left:800px"><div class="contact-icon">
  <svg width="28" height="28" viewBox="0 0 28 28" fill="none" stroke="#f2a21d" stroke-width="2"><rect x="3" y="7" width="22" height="15"/><path d="M3 7l11 9 11-9"/></svg></div>
  <div class="contact-text">Email id<br>contact@tevrixbim.com</div></div>

<!-- footer -->
<footer class="footer"></footer>
<div class="abs foot-brand"><div class="name"><i></i>Tevrix</div><div class="tag">BIM CONSULTING</div></div>
<p class="abs foot-about">Lorem Ipsum is simply dummy text of the printing and typesetting industry.</p>
<h4 class="foot-h" style="left:418px">Our Services</h4>
<ul class="foot-list" style="left:418px"><li>Architecture</li><li>Construction</li><li>Interior Design</li><li>Exterior Design</li><li>Repairing</li></ul>
<ul class="foot-list" style="left:570px"><li>Metal Roofing</li><li>Construction Consultant</li><li>Green Building</li><li>Laminate Flooring</li><li>House Renovation</li></ul>
<h4 class="foot-h" style="left:770px">Recent Post</h4>
<div class="recent" style="top:3180px"><h5>Lorem Ipsum is simply</h5><p>Reference site about Lorem Ipsum, giving information on its origins</p></div>
<div class="recent" style="top:3250px"><h5>Lorem Ipsum is simply</h5><p>Reference site about Lorem Ipsum, giving information on its origins</p></div>
<div class="copyright">Copyright © 2017 Tevrixbimconsulting. All Rights Reserved</div>

</body>
</html>
```